Vehicle van signage design bright lane tow business

Require a vehicle signage design that will be used to wrap a van.

I specialise in removal of fuel from people when they have filled their car with the incorrect fuel. Also in addition i provide services for contaminated fuel removal, out of fuel assist and stale fuel removal. I have a logo design already and web site done and require signage design for the van. The signage design must have the following

My logo - uploaded in files in colour and grey scale
Contact number - 0438215094
Web site link - www.brightlanetow.com.au
Text - 24/7 Road side assist
Text - Filled your vehicle with the wrong fuel?

Van photos provided in files on the project portfolio with the side, front and rear view.

If further assistance is required I am happy to help and provide more input.

Target Market(s)

Customers requiring road side assist when filled vehicle with wrong fuel

Industry/Entity Type

Business

Requirements
Must have
• My logo - uploaded in files in colour and grey scale
• Contact number - 0438215094
• Web site link - www.brightlanetow.com.au
• Text - 24/7 Road side assist
• Text - Filled your vehicle with the wrong fuel?

```html
<!DOCTYPE html>
<html lang="en">
<head>
<meta charset="utf-8">
<title>Bright Lane Tow – Van Side Wrap</title>
<link rel="stylesheet" href="https://fonts.googleapis.com/css2?family=Black+Ops+One&family=Montserrat:ital,wght@0,700;1,600&family=Roboto+Condensed:wght@700&display=swap">
<style>
  :root {
    --page: #ffffff;
    --body-white: #f4f5f7;
    --trim-dark: #1e1f22;
    --window-black: #0c0d0f;
    --brand-purple: #5454c8;
    --brand-orange: #f07a1e;
    --brand-blue: #1f74c9;
    --word-grey: #4a4b4f;
    --text-white: #ffffff;
    --wheel-grey: #8e9196;
  }
  html, body {
    margin: 0;
    width: 1200px;
    height: 1000px;
    overflow: hidden;
    background: var(--page);
  }
  .van-wrap { display: block; width: 1200px; height: 1000px; }
  .body-panel { fill: var(--body-white); stroke: #c9ccd2; stroke-width: 2; }
  .lower-trim { fill: var(--trim-dark); }
  .stripe-purple { fill: var(--brand-purple); }
  .skirt-purple { fill: var(--brand-purple); }
  .window-panel { fill: var(--window-black); }
  .cab-window { fill: var(--window-black); }
  .wheel-tyre { fill: #151515; }
  .wheel-rim { fill: var(--wheel-grey); }
  .panel-line { stroke: #b7bac0; stroke-width: 2; fill: none; }
  .tagline-assist {
    font-family: "Montserrat", sans-serif; font-weight: 700;
    font-size: 19px; fill: var(--text-white); letter-spacing: 0.5px;
  }
  .headline {
    font-family: "Black Ops One", sans-serif;
    font-size: 31px; fill: var(--text-white);
  }
  .brand-mark { fill: var(--brand-blue); }
  .brand-name {
    font-family: "Montserrat", sans-serif; font-weight: 700;
    font-size: 30px; fill: var(--word-grey); letter-spacing: 1px;
  }
  .phone-number {
    font-family: "Roboto Condensed", sans-serif; font-weight: 700;
    font-size: 40px; fill: var(--brand-orange);
  }
  .phone-icon-ring { fill: none; stroke: var(--brand-orange); stroke-width: 3.5; }
  .phone-icon-handset { fill: var(--brand-orange); }
  .web-address {
    font-family: "Montserrat", sans-serif; font-style: italic; font-weight: 600;
    font-size: 17px; fill: var(--text-white); letter-spacing: 1px;
  }
</style>
</head>
<body>
<svg class="van-wrap" viewBox="0 0 1200 1000" xmlns="http://www.w3.org/2000/svg">
  <defs>
    <linearGradient id="orangeFade" x1="0" y1="0" x2="1" y2="0">
      <stop offset="0" stop-color="#f07a1e"/>
      <stop offset="0.75" stop-color="#f07a1e"/>
      <stop offset="1" stop-color="#f07a1e" stop-opacity="0"/>
    </linearGradient>
  </defs>

  <!-- van body -->
  <path class="body-panel" d="M50,645 L52,565 Q58,525 120,495 L225,440 L318,328 Q332,300 372,298 L1112,296 Q1138,298 1142,330 L1150,645 Z"/>

  <!-- cab side window -->
  <path class="cab-window" d="M215,490 L325,345 Q335,335 350,335 L440,335 Q450,335 450,348 L450,470 Z"/>

  <!-- purple sweep -->
  <polygon class="stripe-purple" points="52,548 500,432 1000,312 1112,298 1142,310 1146,484 500,498 56,585"/>
  <!-- orange sweep -->
  <polygon fill="url(#orangeFade)" points="58,572 505,458 565,458 505,488 64,598"/>
  <text class="tagline-assist" transform="translate(158,548) rotate(-13)">24/7 ROAD SIDE ASSIST</text>

  <!-- rear side window panel -->
  <rect class="window-panel" x="497" y="328" width="608" height="152" rx="10"/>
  <line class="panel-line" x1="773" y1="300" x2="773" y2="640"/>
  <line class="panel-line" x1="472" y1="300" x2="472" y2="640"/>

  <!-- brand -->
  <circle class="brand-mark" cx="622" cy="418" r="70"/>
  <text class="brand-name" x="625" y="558" text-anchor="middle">BRIGHT LANE TOW</text>

  <!-- headline -->
  <text class="headline" transform="translate(742,412) rotate(-5)">Filled your vehicle</text>
  <text class="headline" transform="translate(742,452) rotate(-5)">with the wrong fuel ?</text>

  <!-- phone -->
  <g class="phone-contact">
    <circle class="phone-icon-ring" cx="853" cy="543" r="16"/>
    <path class="phone-icon-handset" d="M845,533 q3,-2 5,1 l2,4 q1,2 -1,3 l-2,1 q2,5 7,7 l1,-2 q1,-2 3,-1 l4,2 q3,2 1,5 l-2,2 q-3,2 -8,0 q-9,-4 -12,-13 q-2,-5 1,-8 z"/>
    <text class="phone-number" x="880" y="558">0438215094</text>
  </g>

  <!-- lower trim and skirts -->
  <rect class="lower-trim" x="50" y="600" width="1100" height="45" rx="6"/>
  <polygon class="skirt-purple" points="280,635 840,635 840,685 295,685"/>
  <polygon class="skirt-purple" points="1000,635 1095,635 1095,685 1010,685"/>
  <text class="web-address" x="622" y="664" text-anchor="middle">BRIGHTLANETOW.COM.AU</text>

  <!-- wheels -->
  <circle class="wheel-tyre" cx="195" cy="672" r="62"/>
  <circle class="wheel-rim" cx="195" cy="672" r="38"/>
  <circle class="wheel-tyre" cx="918" cy="684" r="62"/>
  <circle class="wheel-rim" cx="918" cy="684" r="38"/>
</svg>
</body>
</html>
```